"Wellenhafen" private practice for physiotherapy

we are looking for a flyer design for a private practice for physiotherapy. the name of the practice is "Wellenhafen".
Treatments such as: manual therapy, manual lymphatic drainage, classic massage, sectoral alternative practitioners are offered

The flyers should be double-sided and the format DIN long (105x210 mm)

Font styles to use
Serif

Colors
0094D4
00A9DD
6FCCEA
C7EBF8
E9F6FB

Requirements
Must have
• Wellenhafen, Lindenweg 17, 04719 Auental / Wellenhafen-praxis-beispiel.de / Tel. 03471 5820317

```html
<!DOCTYPE html>
<html lang="de">
<head>
<meta charset="utf-8">
<title>Wellenhafen – Flyer</title>
<link rel="stylesheet" href="https://fonts.googleapis.com/css2?family=Mukta:wght@400;500;600;700;800&display=swap">
<style>
  :root {
    --stage: #e7e8ea;
    --navy: #1e3a9a;
    --edge: #2a3590;
    --white: #ffffff;
    --ink: #2e2e33;
    --map-bg: #eef0f2;
    --map-frame: #9ea3ab;
  }
  * { margin: 0; padding: 0; box-sizing: border-box; }
  html, body { width: 1200px; height: 1137px; overflow: hidden; background: var(--stage); }
  body { position: relative; font-family: "Mukta", "Hind", sans-serif; }

  .flyer { position: absolute; top: 90px; width: 478px; height: 956px; overflow: hidden; background: var(--white); }
  .flyer--front { left: 104px; }
  .flyer--back { left: 617px; }
  .flyer__shapes { position: absolute; inset: 0; width: 478px; height: 956px; }

  .brand { position: absolute; color: var(--white); font-weight: 700; font-size: 47px; line-height: 1; letter-spacing: 0.3px; text-shadow: 0 2px 6px rgba(0,0,40,.35); }
  .flyer--front .brand { left: 54px; top: 520px; }
  .flyer--back .brand { left: 0; right: 0; top: 64px; text-align: center; }

  .services { position: absolute; left: 52px; top: 582px; list-style: none; color: var(--white); font-size: 32px; font-weight: 500; line-height: 34.5px; }
  .services li { position: relative; padding-left: 37px; }
  .services .tick { position: absolute; left: 0; top: 4px; width: 30px; height: 30px; }

  .service-grid { position: absolute; left: 0; top: 140px; width: 478px; }
  .service { position: absolute; width: 220px; text-align: center; color: var(--white); font-size: 33px; font-weight: 500; line-height: 37.5px; text-shadow: 0 2px 6px rgba(0,0,40,.35); }
  .service .tick { display: block; width: 54px; height: 54px; margin: 0 auto 8px; }
  .service--a { left: 43px; top: 0; }
  .service--b { left: 231px; top: 2px; }
  .service--c { left: 43px; top: 155px; }
  .service--d { left: 231px; top: 155px; }

  .address { position: absolute; left: 0; right: 0; top: 766px; text-align: center; color: var(--ink); font-size: 32px; font-weight: 500; line-height: 36px; }

  .contact { position: absolute; left: 0; right: 0; top: 845px; text-align: center; color: var(--navy); }
  .contact__web { font-size: 25px; font-weight: 500; line-height: 28px; }
  .contact__phone { font-size: 55px; font-weight: 800; line-height: 60px; letter-spacing: 0.5px; }
</style>
</head>
<body>

<section class="flyer flyer--front">
  <svg class="flyer__shapes" viewBox="0 0 478 956">
    <defs>
      <linearGradient id="front-blue" x1="0" y1="0" x2="1" y2="1">
        <stop offset="0" stop-color="#2f86da"/>
        <stop offset="0.6" stop-color="#1d5fb8"/>
        <stop offset="1" stop-color="#1a3f95"/>
      </linearGradient>
      <linearGradient id="front-photo" x1="0" y1="0" x2="1" y2="1">
        <stop offset="0" stop-color="#eef1f4"/>
        <stop offset="1" stop-color="#aebed0"/>
      </linearGradient>
      <linearGradient id="circle-photo" x1="0" y1="0" x2="1" y2="1">
        <stop offset="0" stop-color="#c9d3dd"/>
        <stop offset="1" stop-color="#6f7d8e"/>
      </linearGradient>
    </defs>
    <rect width="478" height="956" fill="url(#front-blue)"/>
    <path role="img" aria-label="Foto: Therapeut behandelt den Rücken eines Patienten auf der Liege" d="M0 0 H300 C360 50 420 80 478 82 V300 C380 330 200 390 0 425 Z" fill="url(#front-photo)"/>
    <circle role="img" aria-label="Foto: Therapeutin mobilisiert ein Knie" cx="368" cy="276" r="120" fill="url(#circle-photo)" stroke="#5a5f6a" stroke-width="6"/>
    <circle role="img" aria-label="Foto: Behandlung am Knie eines Patienten" cx="260" cy="408" r="100" fill="url(#circle-photo)" stroke="#5a5f6a" stroke-width="6"/>
    <path d="M0 826 C160 812 350 792 478 740 V956 H0 Z" fill="var(--white)"/>
    <path d="M0 826 C160 812 350 792 478 740" fill="none" stroke="var(--edge)" stroke-width="6"/>
  </svg>

  <h1 class="brand">Wellenhafen</h1>
  <ul class="services">
    <li><svg class="tick" viewBox="0 0 30 30"><circle cx="13" cy="16" r="11" fill="none" stroke="#fff" stroke-width="2.6"/><path d="M7.5 15.5 L12.5 21 L27 5" fill="none" stroke="#fff" stroke-width="3" stroke-linecap="round" stroke-linejoin="round"/></svg>Manual Therapy</li>
    <li><svg class="tick" viewBox="0 0 30 30"><circle cx="13" cy="16" r="11" fill="none" stroke="#fff" stroke-width="2.6"/><path d="M7.5 15.5 L12.5 21 L27 5" fill="none" stroke="#fff" stroke-width="3" stroke-linecap="round" stroke-linejoin="round"/></svg>Manual Lymphatic<br>Drainage</li>
    <li><svg class="tick" viewBox="0 0 30 30"><circle cx="13" cy="16" r="11" fill="none" stroke="#fff" stroke-width="2.6"/><path d="M7.5 15.5 L12.5 21 L27 5" fill="none" stroke="#fff" stroke-width="3" stroke-linecap="round" stroke-linejoin="round"/></svg>Classic Massage</li>
    <li><svg class="tick" viewBox="0 0 30 30"><circle cx="13" cy="16" r="11" fill="none" stroke="#fff" stroke-width="2.6"/><path d="M7.5 15.5 L12.5 21 L27 5" fill="none" stroke="#fff" stroke-width="3" stroke-linecap="round" stroke-linejoin="round"/></svg>Sectoral Alternative<br>Practitioners</li>
  </ul>

  <div class="contact">
    <p class="contact__web">Wellenhafen-praxis-beispiel.de</p>
    <p class="contact__phone">03471 5820317</p>
  </div>
</section>

<section class="flyer flyer--back">
  <svg class="flyer__shapes" viewBox="0 0 478 956">
    <defs>
      <linearGradient id="back-blue" x1="0" y1="0" x2="1" y2="1">
        <stop offset="0" stop-color="#2a9ae6"/>
        <stop offset="0.55" stop-color="#2c82dc"/>
        <stop offset="1" stop-color="#1f5fc4"/>
      </linearGradient>
    </defs>
    <path role="img" aria-label="Foto: Patientin erhält eine Schultermassage, blau eingefärbt" d="M0 0 H478 V502 C330 560 150 600 0 594 Z" fill="url(#back-blue)"/>
    <path d="M0 594 C150 600 330 560 478 502" fill="none" stroke="var(--edge)" stroke-width="6"/>
    <rect role="img" aria-label="Stadtplan mit Standort der Praxis" x="65" y="532" width="354" height="202" fill="var(--map-bg)" stroke="var(--map-frame)" stroke-width="5"/>
  </svg>

  <h2 class="brand">Wellenhafen</h2>
  <div class="service-grid">
    <p class="service service--a"><svg class="tick" viewBox="0 0 56 56"><circle cx="25" cy="30" r="22" fill="none" stroke="#fff" stroke-width="4.5"/><path d="M14 29 L24 40 L52 6" fill="none" stroke="#fff" stroke-width="5.5" stroke-linecap="round" stroke-linejoin="round"/></svg>Manual<br>Therapy</p>
    <p class="service service--b"><svg class="tick" viewBox="0 0 56 56"><circle cx="25" cy="30" r="22" fill="none" stroke="#fff" stroke-width="4.5"/><path d="M14 29 L24 40 L52 6" fill="none" stroke="#fff" stroke-width="5.5" stroke-linecap="round" stroke-linejoin="round"/></svg>Classic<br>Massage</p>
    <p class="service service--c"><svg class="tick" viewBox="0 0 56 56"><circle cx="25" cy="30" r="22" fill="none" stroke="#fff" stroke-width="4.5"/><path d="M14 29 L24 40 L52 6" fill="none" stroke="#fff" stroke-width="5.5" stroke-linecap="round" stroke-linejoin="round"/></svg>Sectoral<br>Alternative<br>Practitioners</p>
    <p class="service service--d"><svg class="tick" viewBox="0 0 56 56"><circle cx="25" cy="30" r="22" fill="none" stroke="#fff" stroke-width="4.5"/><path d="M14 29 L24 40 L52 6" fill="none" stroke="#fff" stroke-width="5.5" stroke-linecap="round" stroke-linejoin="round"/></svg>Manual<br>Lymphatic<br>Drainage</p>
  </div>

  <p class="address">Lindenweg 17,<br>04719 Auental</p>

  <div class="contact">
    <p class="contact__web">Wellenhafen-praxis-beispiel.de</p>
    <p class="contact__phone">03471 5820317</p>
  </div>
</section>

</body>
</html>
```